13 Tovi - new website design project

Our company Tovi Electrical is developing a new lead generation website focused on Electrical, LED Lighting and Solar Power. We need a high converting website.

Example of our current website is www.tovielectrical.com.au You can take content from this website for this new design. Our colours are red, black and white. For our new website we would like to promote Tovi, Bright Days Ahead. Please listen to the jingle.

The below link is the company jingle that we have developed.
http://www.tunecraftstudio.com.au/tov-tc-v1/

The key for this brief is to generate leads for Electrical, LED Lighting (for commercial) and Solar Power & Storage.

Target Market(s)

Business owners in Melbourne Victoria

Number of Pages Required

4 page

Colors
ec1f27
ffffff

Requirements
Must have
• This page must be clean, be in line with company branding and a high converting lead website.

```html
<!DOCTYPE html>
<html lang="en">
<head>
<meta charset="utf-8">
<title>Tovi Electrical</title>
<link rel="stylesheet" href="https://fonts.googleapis.com/css2?family=Cinzel:wght@700&family=Questrial&family=Lato:wght@400;700&display=swap">
<style>
:root{
  --red:#d0282e;
  --red-bright:#ec1f27;
  --black:#0a0a0a;
  --ink:#222;
  --grey:#666;
  --light:#f4f4f4;
  --white:#fff;
  --blue:#1a73c9;
}
*{box-sizing:border-box;margin:0;padding:0}
html,body{width:1200px;height:3488px;overflow:hidden;background:var(--white)}
body{font-family:'Lato',sans-serif;color:var(--ink)}
.wrap{width:1046px;margin:0 auto;position:relative}
h2.section-title{font-family:'Questrial',sans-serif;font-weight:400;font-size:40px;text-align:center;color:var(--ink)}

/* header */
.topbar{height:93px}
.topbar .wrap{height:93px;display:flex;align-items:center;justify-content:space-between}
.brand{display:flex;align-items:center;gap:12px;font-family:'Lato',sans-serif;font-weight:700;font-size:40px;color:var(--red)}
.brand-dot{width:30px;height:30px;border-radius:50%;background:var(--red)}
.appointment{display:flex;align-items:center;gap:16px;font-size:18px;color:#555}
.appointment .num{font-size:24px;color:#333;margin-left:4px}
.nav{height:63px;background:var(--red)}
.nav .wrap{display:flex;height:63px}
.nav a{color:var(--white);text-decoration:none;font-family:'Questrial',sans-serif;font-size:20px;display:flex;align-items:center;padding:0 34px}
.nav a.active{background:#2a2a2a}

/* hero */
.hero{height:572px;position:relative;background:linear-gradient(135deg,#6b4a3a 0%,#9a7f6a 35%,#3d5a8f 60%,#7c8a56 85%,#5e6a3c 100%)}
.hero-text{position:absolute;top:155px;left:0;right:0;text-align:center}
.hero-title{font-family:'Cinzel',serif;font-size:80px;color:var(--red-bright);line-height:1}
.hero-sub{font-family:'Cinzel',serif;font-size:32px;color:var(--white);margin-top:14px;letter-spacing:1px}
.btn-dark{display:inline-block;background:var(--black);color:var(--white);font-family:'Questrial',sans-serif;font-size:20px;padding:14px 34px;text-decoration:none}
.hero .btn-dark{margin-top:36px}

/* about */
.about{height:591px;padding-top:58px}
.features{display:flex;justify-content:space-between;margin-top:44px}
.feature{width:244px;text-align:center}
.feature svg{display:block;margin:0 auto}
.feature h3{font-family:'Questrial',sans-serif;font-weight:400;font-size:21px;margin-top:28px}
.feature p{font-size:13.5px;line-height:23px;color:var(--grey);margin-top:12px}
.about .more{text-align:center;margin-top:60px}

/* services */
.services{height:602px;padding-top:50px;background:linear-gradient(180deg,#d8c7a8 0%,#c9b08a 55%,#b48c68 100%)}
.services .intro{font-size:15px;line-height:22px;text-align:center;color:#333;margin:14px auto 0;width:980px}
.cards{display:flex;justify-content:space-between;margin-top:36px}
.card{width:334px}
.card .photo{height:186px}
.card .caption{height:126px;background:var(--black);color:var(--white);text-align:center;padding-top:22px}
.card h3{font-family:'Questrial',sans-serif;font-weight:400;font-size:21px}
.card p{font-size:14px;line-height:21px;margin-top:10px}

/* partners */
.partners{height:282px;position:relative}
.partners .wrap{display:flex;justify-content:space-between;padding-top:52px}
.partner{width:250px}
.partner .name{height:48px;font-family:'Lato',sans-serif;font-weight:700;font-size:24px;color:#333;display:flex;align-items:center;justify-content:center}
.partner .photo{height:102px;margin-top:12px;position:relative;background:linear-gradient(180deg,#9aa2aa,#5e666e)}
.partner .zoom{position:absolute;right:8px;bottom:6px}
.arrow{position:absolute;top:120px}

/* why */
.why{height:402px;position:relative;background:linear-gradient(90deg,#a9bcc2 0%,#b7c8cd 55%,#dfe6e8 100%)}
.why .list{position:absolute;left:77px;top:56px}
.why h2{font-family:'Questrial',sans-serif;font-weight:400;font-size:40px;color:var(--white)}
.why ul{list-style:none;margin-top:28px}
.why li{display:flex;align-items:center;gap:20px;font-size:22px;color:#333;height:52px}
.why .portrait{position:absolute;right:60px;top:30px;width:300px;height:372px;background:linear-gradient(180deg,#cbb9ad,#2a2a2a)}

/* blog */
.blog{height:500px;padding-top:50px}
.blog h2 span{color:var(--blue)}
.posts{display:flex;justify-content:space-between;margin-top:34px}
.post{width:333px}
.post .photo{height:163px}
.post .meta{display:flex;align-items:center;gap:18px;height:34px;margin-top:-18px;padding-left:32px;border-bottom:1px solid #ddd}
.post .avatar{width:52px;height:52px;border-radius:50%;background:#d9dde2;border:3px solid var(--white);margin-top:-14px}
.post .date{font-size:12px;font-style:italic;color:#666}
.post h3{font-weight:400;font-size:21px;margin-top:26px}
.post p{font-size:13.5px;line-height:22px;color:var(--grey);margin-top:6px}
.post a{display:block;font-size:15px;color:var(--red);text-decoration:none;margin-top:12px}

/* footer */
.footer{height:258px;background:var(--black);color:var(--white)}
.footer .links-row{display:flex;justify-content:space-between;align-items:center;height:112px;border-bottom:1px solid #777}
.footer .links a{color:var(--white);text-decoration:none;font-size:17px;margin-right:20px}
.social{display:flex;gap:18px}
.social span{width:46px;height:46px;border-radius:50%;background:var(--white)}
.social span.first{background:var(--red)}
.contacts{display:flex;padding-top:30px}
.contact{display:flex;gap:20px;width:370px}
.contact h4{font-weight:400;font-size:21px}
.contact p{font-size:14px;line-height:20px;margin-top:4px}

.subscribe{height:125px;background:var(--red)}
.subscribe .wrap{display:flex;justify-content:space-between;align-items:center;height:125px}
.sub-form{width:610px;height:60px;background:var(--white);border-radius:30px;display:flex;align-items:center;padding:4px;border:2px solid #222}
.sub-form .field{flex:1;display:flex;align-items:center;gap:12px;padding-left:22px;font-size:19px}
.sub-form .go{background:var(--black);color:var(--white);border-radius:26px;height:100%;padding:0 40px;display:flex;align-items:center;font-size:19px}
.copyright{color:var(--white);font-size:15px;line-height:20px;width:220px}
</style>
</head>
<body>

<header class="topbar">
  <div class="wrap">
    <div class="brand"><span class="brand-dot"></span>Tovi</div>
    <div class="appointment">Call for Appointment
      <svg width="32" height="26" viewBox="0 0 32 26"><path d="M2 10c0-5 6-8 14-8s14 3 14 8l-6 2-2-4H10l-2 4z" fill="var(--red)"/><rect x="7" y="13" width="18" height="11" rx="2" fill="var(--red)"/><circle cx="16" cy="18" r="3" fill="#fff"/></svg>
      <span class="num">139406</span></div>
  </div>
</header>
<nav class="nav"><div class="wrap">
  <a class="active" href="#">HOME</a><a href="#">TOVI STORY</a><a href="#">OUR WORK</a><a href="#">CONTACT US</a>
</div></nav>

<section class="hero" role="img" aria-label="Two electricians in hard hats installing solar panels on a roof">
  <div class="hero-text">
    <div class="hero-title">TOVI</div>
    <div class="hero-sub">ELECTRICAL, LED LIGHTING, SOLAR POWER</div>
    <a class="btn-dark" href="#">CONTACT US NOW</a>
  </div>
</section>

<section class="about"><div class="wrap">
  <h2 class="section-title">About Tovi</h2>
  <div class="features">
    <div class="feature">
      <svg width="150" height="150" viewBox="0 0 150 150"><circle cx="75" cy="75" r="70" fill="none" stroke="var(--red)" stroke-width="5"/><circle cx="75" cy="75" r="46" fill="none" stroke="var(--red)" stroke-width="2"/><path d="M62 58c-4 4-2 14 6 22s18 10 22 6l-6-8-6 3c-4-2-8-6-10-10l3-6z" fill="var(--red)"/></svg>
      <h3>CALL US</h3><p>Lorem Ipsum is simply dummy text of the printing and typesetting industry. Lorem Ipsum has been.</p>
    </div>
    <div class="feature">
      <svg width="150" height="150" viewBox="0 0 150 150"><circle cx="75" cy="75" r="70" fill="none" stroke="var(--red)" stroke-width="5"/><circle cx="75" cy="75" r="46" fill="none" stroke="var(--red)" stroke-width="2"/><path d="M52 75q23-22 46 0q-23 22-46 0z" fill="none" stroke="var(--red)" stroke-width="4"/><circle cx="75" cy="75" r="7" fill="var(--red)"/></svg>
      <h3>SITE ASSESSMENT</h3><p>Lorem Ipsum is simply dummy text of the printing and typesetting industry. Lorem Ipsum has been.</p>
    </div>
    <div class="feature">
      <svg width="150" height="150" viewBox="0 0 150 150"><circle cx="75" cy="75" r="70" fill="none" stroke="var(--red)" stroke-width="5"/><circle cx="75" cy="75" r="46" fill="none" stroke="var(--red)" stroke-width="2"/><path d="M60 60l30 30M90 60L60 90" stroke="var(--red)" stroke-width="6" stroke-linecap="round"/><circle cx="66" cy="66" r="8" fill="none" stroke="var(--red)" stroke-width="4"/></svg>
      <h3>INSTALLATION</h3><p>Lorem Ipsum is simply dummy text of the printing and typesetting industry. Lorem Ipsum has been.</p>
    </div>
    <div class="feature">
      <svg width="150" height="150" viewBox="0 0 150 150"><circle cx="75" cy="75" r="70" fill="none" stroke="var(--red)" stroke-width="5"/><circle cx="75" cy="75" r="46" fill="none" stroke="var(--red)" stroke-width="2"/><ellipse cx="75" cy="78" rx="20" ry="15" fill="var(--red)"/><rect x="66" y="90" width="5" height="8" fill="var(--red)"/><rect x="80" y="90" width="5" height="8" fill="var(--red)"/><rect x="70" y="60" width="10" height="4" fill="var(--red)"/></svg>
      <h3>SAVINGS</h3><p>Lorem Ipsum is simply dummy text of the printing and typesetting industry. Lorem Ipsum has been.</p>
    </div>
  </div>
  <div class="more"><a class="btn-dark" href="#">READ MORE</a></div>
</div></section>

<section class="services"><div class="wrap">
  <h2 class="section-title">Tovi Services</h2>
  <p class="intro">Electrical and Energy Solutions are at the forefront of our company. Tovi Electrical has a long history in Electrical, LED Lighting and Solar Power and just like the Cougar, we will strive to be fierce &amp; agile in an effort to exceed our customer's expectations and develop stronger links with all our business partners &amp; community.</p>
  <div class="cards">
    <div class="card"><div class="photo" role="img" aria-label="Electrician on the phone in front of a power substation" style="background:linear-gradient(135deg,#d9c04a,#8aa3bd)"></div>
      <div class="caption"><h3>ELECTRICAL</h3><p>Lorem Ipsum is simply dummy text of<br>the printing and typesetting industry.</p></div></div>
    <div class="card"><div class="photo" role="img" aria-label="Pendant LED lights glowing" style="background:linear-gradient(180deg,#5a4a3a,#b88a3a)"></div>
      <div class="caption"><h3>LED LIGHTING</h3><p>Lorem Ipsum is simply dummy text of<br>the printing and typesetting industry.</p></div></div>
    <div class="card"><div class="photo" role="img" aria-label="Installer showing a solar panel to a couple" style="background:linear-gradient(135deg,#e7d9c3,#5670a8)"></div>
      <div class="caption"><h3>SOLAR POWER</h3><p>Lorem Ipsum is simply dummy text of<br>the printing and typesetting industry.</p></div></div>
  </div>
</div></section>

<section class="partners">
  <svg class="arrow" style="left:24px" width="30" height="40" viewBox="0 0 30 40"><path d="M24 4L8 20l16 16" fill="none" stroke="var(--red)" stroke-width="7"/></svg>
  <div class="wrap">
    <div class="partner"><div class="name">Harrow Signs</div><div class="photo" role="img" aria-label="Warehouse interior"><svg class="zoom" width="26" height="26" viewBox="0 0 26 26"><circle cx="11" cy="11" r="7" fill="none" stroke="#fff" stroke-width="3"/><path d="M16 16l7 7" stroke="#fff" stroke-width="3"/></svg></div></div>
    <div class="partner"><div class="name">Steelmark</div><div class="photo" role="img" aria-label="Industrial building interior"><svg class="zoom" width="26" height="26" viewBox="0 0 26 26"><circle cx="11" cy="11" r="7" fill="none" stroke="#fff" stroke-width="3"/><path d="M16 16l7 7" stroke="#fff" stroke-width="3"/></svg></div></div>
    <div class="partner"><div class="name">Boardline</div><div class="photo" role="img" aria-label="Store building exterior" style="background:linear-gradient(180deg,#bcd0e4,#c44a4a)"><svg class="zoom" width="26" height="26" viewBox="0 0 26 26"><circle cx="11" cy="11" r="7" fill="none" stroke="#fff" stroke-width="3"/><path d="M16 16l7 7" stroke="#fff" stroke-width="3"/></svg></div></div>
    <div class="partner"><div class="name">Outback Supply</div><div class="photo" role="img" aria-label="Retail store interior"><svg class="zoom" width="26" height="26" viewBox="0 0 26 26"><circle cx="11" cy="11" r="7" fill="none" stroke="#fff" stroke-width="3"/><path d="M16 16l7 7" stroke="#fff" stroke-width="3"/></svg></div></div>
  </div>
  <svg class="arrow" style="right:24px" width="30" height="40" viewBox="0 0 30 40"><path d="M6 4l16 16L6 36" fill="none" stroke="#222" stroke-width="7"/></svg>
</section>

<section class="why">
  <div class="list">
    <h2>Why Choose us?</h2>
    <ul>
      <li><svg width="36" height="20" viewBox="0 0 36 20"><path d="M0 0l36 10L0 20l8-10z" fill="var(--red)"/></svg>Professional service</li>
      <li><svg width="36" height="20" viewBox="0 0 36 20"><path d="M0 0l36 10L0 20l8-10z" fill="var(--red)"/></svg>5 year workmanship guarantee</li>
      <li><svg width="36" height="20" viewBox="0 0 36 20"><path d="M0 0l36 10L0 20l8-10z" fill="var(--red)"/></svg>Value for Money</li>
      <li><svg width="36" height="20" viewBox="0 0 36 20"><path d="M0 0l36 10L0 20l8-10z" fill="var(--red)"/></svg>Environmentally friendly</li>
      <li><svg width="36" height="20" viewBox="0 0 36 20"><path d="M0 0l36 10L0 20l8-10z" fill="var(--red)"/></svg>Fully insured</li>
    </ul>
  </div>
  <div class="portrait" role="img" aria-label="Woman in a scarf and leather jacket looking at her phone"></div>
</section>

<section class="blog"><div class="wrap">
  <h2 class="section-title">Latest <span>Blog</span></h2>
  <div class="posts">
    <div class="post"><div class="photo" role="img" aria-label="Electrician working on wiring" style="background:linear-gradient(135deg,#e8e8e8,#8a9aa8)"></div>
      <div class="meta"><span class="avatar"></span><span class="date">Posted jan 24, 2017</span></div>
      <h3>Lorem Ipsum is simply dummy</h3><p>Lorem Ipsum is simply dummy text of the printing and typesetting industry.</p><a href="#">READ MORE</a></div>
    <div class="post"><div class="photo" role="img" aria-label="Children playing near a power socket" style="background:linear-gradient(135deg,#c9a57a,#e6d4bd)"></div>
      <div class="meta"><span class="avatar"></span><span class="date">Posted jan 24, 2017</span></div>
      <h3>Lorem Ipsum is simply dummy</h3><p>Lorem Ipsum is simply dummy text of the printing and typesetting industry.</p><a href="#">READ MORE</a></div>
    <div class="post"><div class="photo" role="img" aria-label="Solar panels on a house roof under blue sky" style="background:linear-gradient(180deg,#3f78c8,#9a5a3c)"></div>
      <div class="meta"><span class="avatar"></span><span class="date">Posted jan 24, 2017</span></div>
      <h3>Lorem Ipsum is simply dummy</h3><p>Lorem Ipsum is simply dummy text of the printing and typesetting industry.</p><a href="#">READ MORE</a></div>
  </div>
</div></section>

<footer class="footer"><div class="wrap">
  <div class="links-row">
    <div class="links"><a href="#">Home</a><a href="#">Electrical</a><a href="#">Led Lighting</a><a href="#">Solar power</a><a href="#">Career</a><a href="#">Contact</a></div>
    <div class="social"><span class="first"></span><span></span><span></span><span></span></div>
  </div>
  <div class="contacts">
    <div class="contact"><svg width="30" height="44" viewBox="0 0 30 44"><path d="M15 0C6 0 0 7 0 15c0 11 15 29 15 29s15-18 15-29C30 7 24 0 15 0z" fill="#fff"/><circle cx="15" cy="15" r="6" fill="#000"/></svg>
      <div><h4>Tovi Electrical</h4><p>24/88 Carrow Rd Glen Iris<br>VIC 3146</p></div></div>
    <div class="contact"><svg width="48" height="48" viewBox="0 0 48 48"><rect x="4" y="10" width="14" height="34" rx="3" fill="#fff"/><rect x="20" y="4" width="24" height="40" rx="3" fill="#fff"/><rect x="24" y="9" width="16" height="10" fill="#000"/><g fill="#000"><rect x="24" y="24" width="4" height="4"/><rect x="30" y="24" width="4" height="4"/><rect x="36" y="24" width="4" height="4"/><rect x="24" y="31" width="4" height="4"/><rect x="30" y="31" width="4" height="4"/><rect x="36" y="31" width="4" height="4"/></g></svg>
      <div><h4>Call Us</h4><p>139406<br>Customer Support Toll free</p></div></div>
    <div class="contact"><svg width="52" height="44" viewBox="0 0 52 44"><path d="M2 16L26 2l24 14v26H2z" fill="#fff"/><path d="M2 16l24 16 24-16" fill="none" stroke="#000" stroke-width="2"/><rect x="12" y="8" width="28" height="14" fill="#000"/></svg>
      <div><h4>Email Us</h4><p>service@tovielectrical.com</p></div></div>
  </div>
</div></footer>

<section class="subscribe"><div class="wrap">
  <div class="sub-form">
    <div class="field"><svg width="24" height="18" viewBox="0 0 24 18"><rect x="1" y="1" width="22" height="16" fill="none" stroke="#222" stroke-width="2"/><path d="M1 1l11 9 11-9" fill="none" stroke="#222" stroke-width="2"/></svg>Email</div>
    <div class="go">SUBSCRIBE!</div>
  </div>
  <div class="copyright">© TOVI ELECTRICAL<br>2017. All Rights Reserved</div>
</div></section>

</body>
</html>
```